Varnath Consulting Business card design.

See our website www.varnathconsulting-example.com which will give you a good idea of what we are about. The font is called 'Play'.

I'd like a standout business card in keeping with the themes and branding on the website

Target Market(s)

professionals. HR directors

Industry/Entity Type

Business

Contact Information for Business Card

Varnath Consulting PO Box 3917 Tindale Creek NSW 2840 1300 457 318 Gerald Ashbury Principal email: jobs@varnathconsulting-example.com ABN: 31792048663

Font styles to use
Other font styles liked:
• Play

Requirements
Must have
• Must have same design colours and branding as website.
• On back I'd prefer a list of the things we do which appears below the name at the header on the website

```html
<!DOCTYPE html>
<html lang="en">
<head>
<meta charset="utf-8">
<title>Varnath Consulting – Business Card</title>
<link rel="stylesheet" href="https://fonts.googleapis.com/css2?family=Play:wght@400;700&display=swap">
<style>
  :root {
    --navy: #0d2033;
    --blue: #3a8fd0;
    --white: #ffffff;
    --page: #ffffff;
    --edge: #d4d6d9;
  }
  * { box-sizing: border-box; margin: 0; padding: 0; }
  html, body {
    width: 1200px; height: 1000px; overflow: hidden;
    background: var(--page);
    font-family: 'Play', sans-serif;
  }
  .canvas { position: relative; width: 1200px; height: 1000px; }

  .card { position: absolute; left: 327px; width: 550px; height: 343px; overflow: hidden; }

  /* Front */
  .card--front { top: 144px; background: var(--navy); }
  .front__brand {
    position: absolute; left: 0; right: 0; top: 131px;
    text-align: center; color: var(--white);
    font-size: 41px; line-height: 1; letter-spacing: 0; font-weight: 400;
  }
  .front__services {
    position: absolute; left: 0; right: 0; top: 185px;
    text-align: center; color: var(--blue);
    font-size: 12.5px; line-height: 1; letter-spacing: 1px; white-space: nowrap; font-weight: 400;
  }
  .front__services .sep { margin: 0 3px; }

  /* Back */
  .card--back { top: 513px; background: var(--white); border: 1px solid var(--edge); }
  .back__name {
    position: absolute; left: 38px; top: 46px;
    color: var(--navy); font-size: 19px; font-weight: 400; letter-spacing: 1.2px; line-height: 1;
  }
  .back__title {
    position: absolute; left: 38px; top: 69px;
    color: var(--navy); font-size: 13.5px; letter-spacing: 0.5px; line-height: 1;
  }
  .back__phone {
    position: absolute; left: 38px; top: 90px;
    display: flex; align-items: center; gap: 3px;
    color: var(--blue); font-size: 42px; line-height: 1;
  }
  .back__phone svg { width: 31px; height: 31px; fill: var(--navy); }
  .back__email {
    position: absolute; left: 39px; top: 135px;
    color: var(--blue); font-size: 13.5px; letter-spacing: 0.6px; line-height: 1;
  }
  .back__band {
    position: absolute; left: 0; right: 0; bottom: 0; height: 135px;
    background: var(--navy); color: var(--white);
    padding: 26px 0 0 39px;
  }
  .band__brand { font-size: 19px; line-height: 1; letter-spacing: 0.3px; margin-bottom: 2px; }
  .band__lines { font-size: 13.5px; line-height: 14.5px; letter-spacing: 0.8px; }
</style>
</head>
<body>
<main class="canvas">
  <section class="card card--front" aria-label="Card front">
    <h1 class="front__brand">VARNATH CONSULTING</h1>
    <p class="front__services">Search &amp; Select <span class="sep">|</span> Career <span class="sep">|</span> Coaching <span class="sep">|</span> Leadership <span class="sep">|</span> Outplacement</p>
  </section>

  <section class="card card--back" aria-label="Card back">
    <h2 class="back__name">GERALD ASHBURY</h2>
    <p class="back__title">Principal</p>
    <p class="back__phone">
      <svg viewBox="0 0 24 24" aria-hidden="true"><path d="M6.6 10.8c1.4 2.8 3.8 5.1 6.6 6.6l2.2-2.2c.3-.3.7-.4 1-.2 1.1.4 2.3.6 3.6.6.6 0 1 .4 1 1V20c0 .6-.4 1-1 1C10.6 21 3 13.4 3 4c0-.6.4-1 1-1h3.5c.6 0 1 .4 1 1 0 1.3.2 2.5.6 3.6.1.3 0 .7-.2 1l-2.3 2.2z"/></svg>
      <span>1300 457 318</span>
    </p>
    <p class="back__email">jobs@varnathconsulting-example.com</p>
    <div class="back__band">
      <p class="band__brand">VARNATH CONSULTING</p>
      <p class="band__lines">PO Box 3917<br>Tindale Creek NSW 2840<br>ABN 31792048663<br>www.varnathconsulting-example.com</p>
    </div>
  </section>
</main>
</body>
</html>
```